We need a picture for software product. This picture should be place into "About" page and also on product page on site

The product is a plug-in for Vornel Imagetrix. The details are here
http://www.kestrawidgets.com/products/products.php?menu=get_prod_id&prod_id=5

PS. When I said what I need a picture for "About" window then I mean some like
http://velmarond.com/ps/grainforge/img/grainforge.jpg

Reason: I'm ready to wait as long as it needs because I'm interesting to get a desirable result

```html
<!DOCTYPE html>
<html lang="en">
<head>
<meta charset="utf-8">
<title>Grainforge — About Artwork</title>
<link rel="stylesheet" href="https://fonts.googleapis.com/css2?family=Archivo+Black&display=swap">
<style>
  :root {
    --sky-deep: #4a8fd0;
    --sky-light: #b9dcf3;
    --leaf-bright: #86c440;
    --meadow: #7cc424;
    --type-olive: #7da51c;
    --type-lime: #8cb824;
    --type-green: #1fae3c;
    --type-orange: #c8690f;
    --type-title: #a6dc52;
    --type-title-edge: #eaffc8;
  }
  * { margin: 0; padding: 0; box-sizing: border-box; }
  html, body { width: 1200px; height: 1000px; overflow: hidden; background: #ffffff; }
  .canvas { position: relative; width: 1200px; height: 1000px; overflow: hidden; }

  .landscape-art {
    position: absolute; inset: 0;
    background:
      linear-gradient(180deg, transparent 0%, transparent 66%, var(--meadow) 92%),
      linear-gradient(110deg, var(--sky-deep) 0%, var(--sky-light) 45%, var(--leaf-bright) 80%);
  }

  .product-name {
    position: absolute;
    font-family: "Archivo Black", "Arial Black", sans-serif;
    font-weight: 400;
    line-height: 1;
    white-space: nowrap;
  }
  .product-name--orange-top { left: 597px; top: 286px; font-size: 40px; color: var(--type-orange); }
  .product-name--olive-large { left: 430px; top: 322px; font-size: 92px; color: var(--type-olive); }
  .product-name--lime-mid { left: 315px; top: 430px; font-size: 64px; color: var(--type-lime); }
  .product-name--green-large { left: 597px; top: 488px; font-size: 90px; color: var(--type-green); }
  .product-name--orange-low { left: 283px; top: 526px; font-size: 40px; color: var(--type-orange); }
  .product-name--lime-low { left: 305px; top: 572px; font-size: 58px; color: var(--type-olive); }
  .product-name--lime-small { left: 703px; top: 613px; font-size: 38px; color: var(--type-lime); }
  .product-name--title {
    left: 135px; top: 858px; font-size: 110px;
    color: var(--type-title);
    -webkit-text-stroke: 2px var(--type-title-edge);
    text-shadow: 0 0 10px rgba(60,120,10,0.8);
  }
</style>
</head>
<body>
  <main class="canvas">
    <div class="landscape-art" role="img" aria-label="Photo of a green meadow with rolling hills and a single round tree under a blue cloudy sky, the upper right dissolving into green digital squares"></div>

    <span class="product-name product-name--orange-top">Grainforge</span>
    <span class="product-name product-name--olive-large">Grainforge</span>
    <span class="product-name product-name--lime-mid">Grainforge</span>
    <span class="product-name product-name--green-large">Grainforge</span>
    <span class="product-name product-name--orange-low">Grainforge</span>
    <span class="product-name product-name--lime-low">Grainforge</span>
    <span class="product-name product-name--lime-small">Grainforge</span>
    <h1 class="product-name product-name--title">Grainforge</h1>
  </main>
</body>
</html>
```